Redesign of Website

We need an overhaul of our website. I've attached our current logo files. Please visit www.pelvorix.com for our current website for information about our company. We are looking for the same type of website (information-based only) so no need for any online store, payments, interactive stuff or anything like that...basically looking for a fresh new look! Also please make sure this design will be mobile-friendly. Thanks!

```html
<!DOCTYPE html>
<html lang="en">
<head>
<meta charset="utf-8">
<title>Pelvorix Consultants</title>
<link href="https://fonts.googleapis.com/css2?family=Audiowide&family=Roboto:wght@400;500;700&display=swap" rel="stylesheet">
<style>
:root{
  --navy:#132a6b;
  --white:#ffffff;
  --grey-band:#e8e8e8;
  --card-grey:#e6e6e6;
  --text:#222222;
  --footer:#2f3233;
  --map-land:#e9e9e6;
  --map-water:#b7d8f2;
}
*{box-sizing:border-box;margin:0;padding:0}
html,body{width:1200px;height:2469px;overflow:hidden}
body{font-family:"Roboto",Arial,sans-serif;color:var(--text);background:var(--white);position:relative}

.site-header{height:107px;display:flex;align-items:center;justify-content:space-between;padding:0 84px 0 77px}
.brand{font-family:"Audiowide",sans-serif;font-size:30px;color:var(--navy);letter-spacing:2px;white-space:nowrap}
.phone{display:flex;align-items:center;gap:16px;font-size:15px;color:var(--text)}

.main-nav{height:48px;background:var(--navy);display:flex;align-items:center;justify-content:space-between;padding:0 80px 0 92px}
.main-nav ul{list-style:none;display:flex;gap:32px}
.main-nav a{color:var(--white);text-decoration:none;font-size:15px}

.hero{height:515px;position:relative;background:linear-gradient(110deg,#2b4a8c 0%,#4a6aa8 35%,#8b95a8 60%,#c7c3bb 80%,#6d7f9f 100%);display:flex;flex-direction:column;align-items:center;color:var(--white);text-align:center}
.hero::before{content:"";position:absolute;inset:0;background:linear-gradient(180deg,rgba(20,45,110,.55),rgba(20,45,110,.25))}
.hero>*{position:relative}
.hero h1{font-family:"Audiowide",sans-serif;font-weight:400;font-size:34px;margin-top:168px;letter-spacing:1px;white-space:nowrap}
.hero p{font-size:14.5px;line-height:28px;width:780px;margin-top:12px}
.btn{display:inline-block;background:var(--navy);color:var(--white);border-radius:26px;text-decoration:none;font-weight:500;text-align:center}
.hero .btn{margin-top:46px;width:196px;height:50px;line-height:50px;font-size:19px}
.hero .chev{margin-top:72px}

.about{height:376px;background:var(--grey-band);position:relative;padding:58px 0 0 76px}
.about h2{font-family:"Audiowide",sans-serif;font-weight:400;font-size:29px;line-height:40px;color:var(--navy);letter-spacing:1px;white-space:nowrap;width:630px}
.about .copy{width:630px;margin-top:22px}
.about p{font-size:15px;line-height:18px;margin-bottom:13px;color:var(--text)}
.about .btn{margin-top:18px;width:149px;height:41px;line-height:41px;font-size:15px}
.about .photo{position:absolute;left:729px;top:54px;width:397px;height:268px;background:linear-gradient(160deg,#b57a3c,#7a5a3a 45%,#c9c4b8 70%,#8a5a2a)}

.services{height:669px;text-align:center;position:relative}
.services h2{font-family:"Audiowide",sans-serif;font-weight:400;font-size:40px;color:var(--navy);padding-top:55px;letter-spacing:1px}
.cards{position:absolute;top:146px;left:76px;display:flex;gap:30px}
.card{width:240px;height:400px;background:var(--card-grey);padding:10px;color:var(--text)}
.card .thumb{height:155px}
.card h3{font-size:19px;line-height:28px;font-weight:500;color:var(--navy);margin-top:14px;height:56px}
.card .rule{width:36px;height:2px;background:var(--navy);margin:14px auto 16px}
.card p{font-size:14px;line-height:22px;padding:0 6px}
.card.active{background:var(--navy);color:var(--white)}
.card.active h3{color:var(--white)}
.card.active .rule{background:var(--white)}
.slider-arrows{position:absolute;top:582px;left:583px}

.location{height:446px;position:relative}
.location .map{position:absolute;inset:0;background:linear-gradient(135deg,var(--map-land) 0%,#efefec 45%,var(--map-water) 75%,var(--map-land) 100%)}
.address-card{position:absolute;left:492px;top:239px;width:376px;height:128px;display:flex}
.address-card .photo{width:127px;background:linear-gradient(180deg,#4a4e52,#2e3236)}
.address-card .info{flex:1;background:var(--navy);color:var(--white);padding:20px 0 0 24px;display:flex;gap:14px;font-size:15px;line-height:27px;font-weight:500;white-space:nowrap}

.site-footer{height:308px;background:var(--footer);text-align:center;color:var(--white)}
.site-footer .brand{color:#d8d8d8;font-size:27px;padding-top:56px}
.site-footer ul{list-style:none;display:flex;justify-content:center;gap:38px;margin-top:33px}
.site-footer a{color:var(--white);text-decoration:none;font-size:15px}
.socials{display:flex;justify-content:center;gap:34px;margin-top:26px}
.socials span{width:12px;height:12px;border-radius:50%;background:var(--white)}
.copyright{font-size:14px;margin-top:30px}
</style>
</head>
<body>
<header class="site-header">
  <div class="brand">PELVORIX CONSULTANTS</div>
  <div class="phone">
    <svg width="14" height="14" viewBox="0 0 24 24"><path fill="#222" d="M6.6 10.8a15.1 15.1 0 0 0 6.6 6.6l2.2-2.2c.3-.3.7-.4 1-.2 1.1.4 2.3.6 3.6.6.6 0 1 .4 1 1V20c0 .6-.4 1-1 1A17 17 0 0 1 3 4c0-.6.4-1 1-1h3.5c.6 0 1 .4 1 1 0 1.3.2 2.5.6 3.6.1.3 0 .7-.2 1z"/></svg>
    Call Us : 555-014-2290
  </div>
</header>

<nav class="main-nav">
  <ul>
    <li><a href="#">Home</a></li>
    <li><a href="#">About us</a></li>
    <li><a href="#">Services</a></li>
    <li><a href="#">Contact</a></li>
  </ul>
  <svg width="16" height="16" viewBox="0 0 24 24"><circle cx="10" cy="10" r="6.5" fill="none" stroke="#fff" stroke-width="3"/><line x1="15" y1="15" x2="21" y2="21" stroke="#fff" stroke-width="3.2" stroke-linecap="round"/></svg>
</nav>

<section class="hero" role="img" aria-label="Modern apartment building with balconies under a blue sky">
  <h1>PROPERTY CONDITION REPORTS</h1>
  <p>Before moving ahead on any loan approval, financial institutions need to know the condition of existing structures. Our professional staff will give you the details you need to make sound business decisions.</p>
  <a class="btn" href="#">LEARN MORE</a>
  <svg class="chev" width="16" height="10" viewBox="0 0 16 10"><path d="M2 2l6 6 6-6" fill="none" stroke="#fff" stroke-width="2.5"/></svg>
</section>

<section class="about">
  <h2>PELVORIX CONSULTANTS, INC.</h2>
  <div class="copy">
    <p>With over 25 years experience we provide customized and comprehensive inspection services to financial institutions involved in construction and loan management in New York, New Jersey, Pennsylvania and surrounding areas.</p>
    <p>The firm's professional staff bring years of engineering, environmental, building, and real estate experience to work for our clients.</p>
    <p>Pelvorix provides our clients with in-depth plan &amp; cost, construction funding, environmental and property condition reports.</p>
  </div>
  <a class="btn" href="#">READ MORE</a>
  <div class="photo" role="img" aria-label="White house on a tree-lined street with autumn leaves"></div>
</section>

<section class="services">
  <h2>SERVICES</h2>
  <div class="cards">
    <article class="card active">
      <div class="thumb" role="img" aria-label="Multi-storey stone and brick residential building" style="background:linear-gradient(180deg,#8fa3bf,#8a7560 55%,#5a6a48)"></div>
      <h3>PROPERTY CONDITION REPORTS</h3>
      <div class="rule"></div>
      <p>Before moving ahead on any loan approval, financial institutions need to know the condition of existing structures.</p>
    </article>
    <article class="card">
      <div class="thumb" role="img" aria-label="Large newly built estate home with lawn" style="background:linear-gradient(180deg,#2f4f8f,#c9bfa8 50%,#4f7a3a)"></div>
      <h3>PLAN &amp; COST REVIEWS</h3>
      <div class="rule"></div>
      <p>Our Plan &amp; Cost Reviews provide lending institutions with expert analysis of new construction projects before loan commitments are made.</p>
    </article>
    <article class="card">
      <div class="thumb" role="img" aria-label="House under construction with scaffolding" style="background:linear-gradient(180deg,#b9c6c0,#c8a340 45%,#6f6a55)"></div>
      <h3>CONSTRUCTION FUNDING INSPECTIONS</h3>
      <div class="rule"></div>
      <p>Lending institutions rarely have employees with the expertise needed to evaluate multiple stages of site construction and ensure that projects</p>
    </article>
    <article class="card">
      <div class="thumb" role="img" aria-label="Old oil storage tank in a basement" style="background:linear-gradient(180deg,#7a736c,#4a403a 50%,#8d8880)"></div>
      <h3>ENVIRONMENTAL TRANSACTION SCREENS</h3>
      <div class="rule"></div>
      <p>Environmental Transaction Screens provide an economical but meaningful alternative for smaller properties such as mixed used buildings,</p>
    </article>
  </div>
  <svg class="slider-arrows" width="34" height="18" viewBox="0 0 34 18"><path d="M10 2L3 9l7 7M24 2l7 7-7 7" fill="none" stroke="#111" stroke-width="3"/></svg>
</section>

<section class="location">
  <div class="map" role="img" aria-label="Street map of the office area beside a lake"></div>
  <div class="address-card">
    <div class="photo" role="img" aria-label="Office building exterior with parked cars"></div>
    <div class="info">
      <svg width="12" height="16" viewBox="0 0 12 16" style="margin-top:6px;flex:none"><path d="M6 0a6 6 0 0 0-6 6c0 4.5 6 10 6 10s6-5.5 6-10a6 6 0 0 0-6-6z" fill="#fff"/><circle cx="6" cy="6" r="2.2" fill="#132a6b"/></svg>
      <div>118 Larkmoor Ave<br>Suite 205, Dell Township,<br>NJ 07990.</div>
    </div>
  </div>
</section>

<footer class="site-footer">
  <div class="brand">PELVORIX CONSULTANTS</div>
  <ul>
    <li><a href="#">Home</a></li>
    <li><a href="#">About us</a></li>
    <li><a href="#">Services</a></li>
    <li><a href="#">Contact Us</a></li>
  </ul>
  <div class="socials" aria-label="Social links"><span></span><span></span><span></span></div>
  <p class="copyright">© Copyright 2019 - www.pelvorix.com</p>
</footer>
</body>
</html>
```